NEW site with a tech flair and a feeling of moving forward!!

Hello Everyone,

We are starting with a small project to get the first 3-4 pages done. The winning designer will have an opportunity to work with us to design out the rest of the site. We estimate there will be between 15 and 20 total pages for the site (so there would probably be more work for the winner)!

We need a new website design to enhance the "coolness" factor of our brand image! Our current website is www.lantavoxmail.com and it needs some updating!

We envision a website where the homepage would be almost a landing page. It might have a 60 second video at the top, or a picture slider and contact info/site map at the bottom. In the middle we envision having the 3 service logos along with a quick summary of each service!

We have 3 main services: Tally On, Shape On and Sendra On. We want to replace those names with our new service names which are: qVantor, qRelbex and qTri-Weld. Each service has its own unique logo! :)

If you look at www.lantavoxmail.com and notice the Tally On / Shape On / Sendra On - - basically we are replacing those names with qVantor / qRelbex / and qTri-Weld. Then we just want to freshen things up - for example, the current information listed under "Tally On" is "good" ...it just doesn't look "cool" ... we need a better way to display it. We provide complex services (and a lot of different services) and are hoping to make a new website that has a feel of being clean, modern, professional, with a technology flair and easy to use/understand our services.

The person visiting the website could watch the 60 second video to get an overview and then click on a logo for their desired service to be able to learn more. Once the user clicks a logo for the desired service, a new page would open and the user could then learn about the service.

After submitting a design for the homepage, please work on a design to totally revamp the "Tally On" page. We don't like the way that is laid out and need to freshen it up. Note: the layout we choose for Tally On will be similar for Sendra On and Shape On.

The perfect website will have a combo of a technology flair, a feeling of moving forward and/or of connecting people/things/information together. The website should convey trust.

ABOUT LANTA VOXMAIL

We are a technology and communications company. We receive data files, print, fold, insert and mail invoices, statements and other important notices. We also deliver via email, SMS/Text Message and IVR Phone calls. Finally we offer an online website where customers can go to pay their invoices. It is important that the website have a clean, modern, professional and technology look/feel.

We also provide marketing and advertising services through the mail and digitally.

**Please note, our main company is called Lanta Voxmail...we have uploaded our 2 new logos (for your reference) for qVantor and qRelbex for reference.

Please message me with any questions! Thanks everyone, looking forward to seeing the designs!

Target Market(s)

Financial companies, Healthcare and Utilities.

Industry/Entity Type

Tech

Number of Pages Required

5+ page

Requirements
Must have
• The perfect website will have a combo of a technology flair, a feeling of moving forward and/or of connecting people/things/information together. The website should convey trust.
Nice to have
• Taking our complicated services and products and making them really simple and easy to understand by using graphs, charts, pictures and other illustrations.
• Eye catchy feel. Needs to be simple. Conveys trustworthy feel.
Should not have
• Can't be boring and bland. Can't be too complex.

```html
<!DOCTYPE html>
<html lang="en">
<head>
<meta charset="utf-8">
<title>Lanta Voxmail</title>
<link rel="stylesheet" href="https://fonts.googleapis.com/css2?family=Open+Sans:ital,wght@0,300;0,400;0,600;0,700;1,400&display=swap">
<style>
:root{
  --blue:#1687d9;
  --blue-dark:#0b5fa8;
  --blue-mid:#0f74c4;
  --navy:#1c3a66;
  --footer:#0d3d74;
  --footer-deep:#0a3263;
  --text:#4a4f57;
  --muted:#8a9099;
  --line:#d6dbe2;
  --bg-soft:#eef1f4;
}
*{box-sizing:border-box;margin:0;padding:0}
html,body{width:1200px;height:3124px;overflow:hidden}
body{font-family:"Open Sans",Arial,sans-serif;color:var(--text);background:#fff;position:relative}
.abs{position:absolute}

/* hero */
.hero-photo{left:0;top:0;width:1200px;height:720px;background:linear-gradient(160deg,#f4f6f8 0%,#dfe4ea 45%,#c9d1da 75%,#e8ecf0 100%)}
.nav{left:0;top:0;width:1200px;height:72px;background:rgba(255,255,255,.82)}
.nav a{position:absolute;top:24px;font-size:15px;color:var(--navy);text-decoration:none}
.nav a.active{color:var(--blue);border-bottom:3px solid var(--blue);padding-bottom:6px}
.brand{position:absolute;left:460px;top:14px;width:280px;height:48px;display:flex;align-items:center;justify-content:center;gap:10px}
.brand-dot{width:22px;height:22px;border-radius:50%;background:var(--blue)}
.brand-name{font-size:30px;font-weight:300;color:var(--blue);letter-spacing:.5px}

.services{left:80px;top:480px;width:1040px;height:280px;display:flex}
.service{flex:1;position:relative;color:#fff;padding:40px 28px 0}
.service:nth-child(1){background:var(--blue)}
.service:nth-child(2){background:var(--blue-dark)}
.service:nth-child(3){background:var(--blue-mid)}
.service .num{position:absolute;left:-4px;top:40px;font-size:96px;font-weight:700;color:rgba(255,255,255,.12);line-height:1}
.service h2{position:relative;font-size:36px;font-weight:400;margin-bottom:18px}
.service p{position:relative;font-size:14px;line-height:1.55}
.service .go{position:absolute;right:24px;bottom:24px}

/* section heads */
.head{width:1200px;text-align:center;font-size:44px;font-weight:400;color:var(--navy);letter-spacing:1px}
.head span{color:var(--blue)}
.head-rule{left:520px;width:160px;height:2px;background:var(--blue)}

/* about */
.video{left:72px;top:912px;width:368px;height:188px;background:linear-gradient(135deg,#e8ebef,#b9c2cc 60%,#8d98a6)}
.video-bar{left:72px;top:1070px;width:368px;height:30px;background:rgba(20,20,20,.75)}
.about-text{left:468px;top:900px;width:652px;font-size:15px;line-height:1.6}
.about-text p{margin-bottom:14px}
.about-text p.lead{color:var(--blue);font-weight:600}
.btn{display:inline-block;background:var(--blue-dark);color:#fff;font-size:16px;padding:10px 22px;border-radius:3px}

/* why */
.why-bg{left:0;top:1160px;width:1200px;height:440px;background:linear-gradient(180deg,#f1f3f6,#dde2e8)}
.cards{left:72px;top:1288px;width:1056px;height:252px;display:flex;gap:14px}
.card{flex:1;background:#fff;box-shadow:0 2px 8px rgba(0,0,0,.12);padding:22px 22px;position:relative}
.card h3{font-size:18px;font-weight:400;color:var(--blue);margin:10px 0 8px}
.card p{font-size:14px;line-height:1.5;color:var(--muted)}
.card .go{position:absolute;right:16px;bottom:16px}

/* testimonial */
.avatar{left:545px;top:1690px;width:110px;height:110px;border-radius:50%;background:linear-gradient(135deg,#e9e4df,#c7bdb3);border:4px solid #fff;box-shadow:0 1px 6px rgba(0,0,0,.2)}
.quote-mark{left:248px;top:1776px;font-size:80px;color:var(--line);font-family:Georgia,serif}
.quote{left:260px;top:1826px;width:680px;font-size:15px;line-height:1.6;font-style:italic;text-align:left}
.who{left:700px;top:1944px;width:240px;text-align:right;font-size:14px}
.who b{color:var(--blue);font-weight:400;font-style:italic}
.dots{left:568px;top:1996px;display:flex;gap:10px}
.dots i{width:12px;height:4px;background:var(--line)}
.dots i.on{background:var(--blue)}

/* request */
.req-bg{left:0;top:2050px;width:1200px;height:390px;background:linear-gradient(90deg,#ffffff 0%,#f4f5f7 45%,#d7dce2 100%)}
.req-intro{left:140px;top:2184px;width:300px;font-size:14px;line-height:1.55}
.req-intro h4{font-size:22px;font-weight:400;color:var(--navy);margin-bottom:14px}
.field{background:#fff;border:1px solid var(--line);height:34px;font-size:13px;color:var(--muted);padding:8px 12px}
.form-col{left:462px;top:2190px;width:300px;display:flex;flex-direction:column;gap:10px}
.textarea{left:772px;top:2190px;width:290px;height:122px;align-items:flex-start}
.send{left:462px;top:2330px;width:300px;height:38px;background:var(--blue-dark);color:#fff;font-size:16px;text-align:center;line-height:38px;letter-spacing:.5px}

/* contact */
.contact{left:80px;top:2480px;width:1040px;display:flex}
.contact-col{flex:1;text-align:center}
.contact-col h5{font-size:32px;font-weight:400;color:var(--blue);margin:8px 0 10px}
.contact-col p{font-size:14px;line-height:1.6}
.contact-col .link{color:var(--blue)}

/* footer */
.footer{left:0;top:2760px;width:1200px;height:328px;background:var(--footer);color:#fff}
.fcol{position:absolute;top:36px}
.fcol h6{font-size:18px;font-weight:400;letter-spacing:1px;margin-bottom:22px}
.news{display:flex;gap:12px;margin-bottom:18px;font-size:14px;line-height:1.45}
.news .thumb{width:60px;height:60px;flex:none;background:linear-gradient(135deg,#5a84b5,#2c5a90)}
.news small{display:block;color:#a9c3e2;font-size:12px}
.f-field{width:300px;height:38px;background:#fff;color:var(--muted);font-size:13px;padding:10px 12px;margin:14px 0 10px}
.f-btn{width:300px;height:40px;border:2px solid #fff;text-align:center;line-height:36px;font-size:16px;letter-spacing:1px}
.social{width:310px;height:40px;border-bottom:1px solid rgba(255,255,255,.18);display:flex;align-items:center;gap:14px;font-size:14px;color:#cfe0f3}
.social i{width:20px;height:20px;border-radius:50%;background:rgba(255,255,255,.3)}
.copy{left:0;top:3088px;width:1200px;height:36px;background:var(--footer-deep);color:#cfe0f3;font-size:13px;text-align:center;line-height:36px}
</style>
</head>
<body>

<!-- Hero -->
<div class="abs hero-photo" role="img" aria-label="Photo of hands working with a laptop and calculator on a bright desk"></div>
<nav class="abs nav">
  <a class="active" href="#" style="left:80px">Home</a>
  <a href="#" style="left:165px">qVantor</a>
  <a href="#" style="left:262px">qRelbex</a>
  <div class="brand"><i class="brand-dot"></i><span class="brand-name">Lanta Voxmail</span></div>
  <a href="#" style="left:830px">qTri-Weld</a>
  <a href="#" style="left:950px">Security</a>
  <a href="#" style="left:1040px">Industries</a>
</nav>

<section class="abs services">
  <div class="service"><span class="num">01</span><h2>qVantor</h2><p>Processing bills is a cumbersome task for many companies. Let us take the work and worry out of that process.</p>
    <svg class="go" width="22" height="22" viewBox="0 0 22 22"><circle cx="11" cy="11" r="10" fill="none" stroke="#fff" stroke-width="1.5"/><path d="M7 11h8M12 7.5l3.5 3.5-3.5 3.5" fill="none" stroke="#fff" stroke-width="1.5"/></svg></div>
  <div class="service"><span class="num">02</span><h2>qRelbex</h2><p>Our full suite of marketing tools will put you on the cutting edge with timely communications to your customers.</p>
    <svg class="go" width="22" height="22" viewBox="0 0 22 22"><circle cx="11" cy="11" r="10" fill="none" stroke="#fff" stroke-width="1.5"/><path d="M7 11h8M12 7.5l3.5 3.5-3.5 3.5" fill="none" stroke="#fff" stroke-width="1.5"/></svg></div>
  <div class="service"><span class="num">03</span><h2>qTri-Weld</h2><p>Take advantage of custom tailored solutions and save time and money by outsourcing.</p>
    <svg class="go" width="22" height="22" viewBox="0 0 22 22"><circle cx="11" cy="11" r="10" fill="none" stroke="#fff" stroke-width="1.5"/><path d="M7 11h8M12 7.5l3.5 3.5-3.5 3.5" fill="none" stroke="#fff" stroke-width="1.5"/></svg></div>
</section>

<!-- About -->
<h2 class="abs head" style="top:790px">ABOUT <span>US</span></h2>
<div class="abs head-rule" style="top:852px"></div>
<div class="abs video" role="img" aria-label="Video still of a business meeting"></div>
<svg class="abs" style="left:224px;top:962px" width="64" height="46" viewBox="0 0 64 46"><rect width="64" height="46" rx="10" fill="#1b1b1b" opacity=".85"/><path d="M26 14l16 9-16 9z" fill="#fff"/></svg>
<div class="abs video-bar"></div>
<svg class="abs" style="left:82px;top:1078px" width="348" height="14" viewBox="0 0 348 14"><path d="M2 2l8 5-8 5z" fill="#fff"/><rect x="22" y="6" width="230" height="3" fill="#777"/><rect x="22" y="6" width="70" height="3" fill="#e33"/><rect x="300" y="3" width="12" height="8" fill="none" stroke="#fff"/><rect x="322" y="2" width="18" height="10" fill="none" stroke="#fff"/></svg>
<div class="abs about-text">
  <p class="lead">Lanta Voxmail is the leading source for providing high quality Business Communication Services, offline and online.</p>
  <p>We are a technology and communications company. We receive data files, print, fold, insert and mail invoices, statements and other important notices. We also deliver via email, SMS/Text Message and IVR Phone calls.</p>
  <p>Vision and Mission statements come and go but our values live on. We start with the timeless value of Integrity. It affects everything we do and stand for.</p>
  <span class="btn">READ MORE</span>
</div>

<!-- Why choose us -->
<div class="abs why-bg" role="img" aria-label="Soft office background with paperwork"></div>
<h2 class="abs head" style="top:1206px">WHY CHOOSE <span>US?</span></h2>
<div class="abs head-rule" style="top:1268px"></div>
<section class="abs cards">
  <div class="card">
    <svg width="40" height="40" viewBox="0 0 40 40"><path d="M6 18h7v18H6zM15 18l7-12c3 0 4 2 3 6l-1 5h10c2 0 3 2 2 4l-4 13H15z" fill="var(--blue)"/></svg>
    <h3>Customer Services</h3><p>Our services save people money and solve their problems quickly.</p>
    <svg class="go" width="22" height="22" viewBox="0 0 22 22"><circle cx="11" cy="11" r="10" fill="none" stroke="#555" stroke-width="1.5"/><path d="M7 11h8M12 7.5l3.5 3.5-3.5 3.5" fill="none" stroke="#555" stroke-width="1.5"/></svg></div>
  <div class="card">
    <svg width="40" height="40" viewBox="0 0 40 40"><path d="M4 15h8l18-9v28l-18-9H4zM10 25l3 10h5l-3-10z" fill="#222"/></svg>
    <h3>Marketing Expertise</h3><p>Our services save people money and solve their problems.</p>
    <svg class="go" width="22" height="22" viewBox="0 0 22 22"><circle cx="11" cy="11" r="10" fill="none" stroke="#555" stroke-width="1.5"/><path d="M7 11h8M12 7.5l3.5 3.5-3.5 3.5" fill="none" stroke="#555" stroke-width="1.5"/></svg></div>
  <div class="card">
    <svg width="40" height="40" viewBox="0 0 40 40"><path d="M10 6v26M4 26l6 7 6-7M28 34V8M22 14l6-7 6 7" fill="none" stroke="#333" stroke-width="3"/></svg>
    <h3>Sorting Expertise</h3><p>Our services save people money and solve their problems.</p>
    <svg class="go" width="22" height="22" viewBox="0 0 22 22"><circle cx="11" cy="11" r="10" fill="none" stroke="#555" stroke-width="1.5"/><path d="M7 11h8M12 7.5l3.5 3.5-3.5 3.5" fill="none" stroke="#555" stroke-width="1.5"/></svg></div>
  <div class="card">
    <svg width="40" height="40" viewBox="0 0 40 40"><rect x="8" y="4" width="24" height="32" fill="none" stroke="#333" stroke-width="3"/><path d="M13 13h14M13 19h14M13 25h9" stroke="#333" stroke-width="2.5"/></svg>
    <h3>Billing Expertise</h3><p>Our services save people money and solve their problems.</p>
    <svg class="go" width="22" height="22" viewBox="0 0 22 22"><circle cx="11" cy="11" r="10" fill="none" stroke="#555" stroke-width="1.5"/><path d="M7 11h8M12 7.5l3.5 3.5-3.5 3.5" fill="none" stroke="#555" stroke-width="1.5"/></svg></div>
</section>

<!-- Testimonial -->
<h2 class="abs head" style="top:1622px">CLIENT <span>TESTIMONIAL</span></h2>
<div class="abs head-rule" style="top:1682px"></div>
<div class="abs avatar" role="img" aria-label="Portrait of the client"></div>
<div class="abs quote-mark">&ldquo;</div>
<p class="abs quote">&ldquo;Our firm counts on Lanta Voxmail to mail our quarterly Market Letters, annual reports and other communication that is critical to our client service and growth strategy. Over the past years we have relied on their prompt, professional service as well as their creative problem solving. Reaching out to our clients and other stakeholders in an efficient and effective manner is essential to our business.&rdquo;</p>
<p class="abs who"><b>- Dana Whitfield</b><br>Senior Vice President</p>
<div class="abs dots"><i class="on"></i><i></i><i></i></div>

<!-- Request call back -->
<div class="abs req-bg" role="img" aria-label="Photo of a person making a phone call at a desk"></div>
<h2 class="abs head" style="top:2108px">REQUEST <span>CALL BACK</span></h2>
<div class="abs head-rule" style="top:2168px"></div>
<div class="abs req-intro"><h4>We'd love to hear from you.</h4><p>Fill out the form below to send us a message. We'd love to hear from you, whether you have questions, comments or just want to say hi.</p></div>
<div class="abs form-col"><div class="field">Name</div><div class="field">Email Id</div><div class="field">Tel. No.</div></div>
<div class="abs field textarea">Have any questions?</div>
<div class="abs send">SEND REQUEST</div>

<!-- Contact -->
<section class="abs contact">
  <div class="contact-col">
    <svg width="48" height="52" viewBox="0 0 48 52"><path d="M24 4c-8 0-14 6-14 14 0 10 14 24 14 24s14-14 14-24c0-8-6-14-14-14z" fill="none" stroke="var(--blue)" stroke-width="3.5"/><circle cx="24" cy="18" r="5" fill="var(--blue)"/><path d="M6 48h36" stroke="var(--blue)" stroke-width="3.5"/></svg>
    <h5>Contact Us</h5><p>418 Alder Row<br>Fernvale, OR 97001<br><span class="link">customerservice@lantavoxmail.com</span></p></div>
  <div class="contact-col">
    <svg width="48" height="52" viewBox="0 0 48 52"><circle cx="24" cy="29" r="18" fill="none" stroke="var(--blue)" stroke-width="3.5"/><path d="M24 29V18M24 29l7 5M19 5h10M24 5v6" stroke="var(--blue)" stroke-width="3.5" fill="none"/></svg>
    <h5>Business Time</h5><p>Mon - Fri : 8:00 a.m To 7:00 p.m<br>Sat - Sun : Off</p></div>
  <div class="contact-col">
    <svg width="48" height="52" viewBox="0 0 48 52"><rect x="5" y="9" width="38" height="38" fill="none" stroke="var(--blue)" stroke-width="3.5"/><path d="M5 19h38M14 4v9M34 4v9" stroke="var(--blue)" stroke-width="3.5"/><path d="M12 26h6v5h-6zM21 26h6v5h-6zM30 26h6v5h-6zM12 35h6v5h-6zM21 35h6v5h-6z" fill="var(--blue)"/></svg>
    <h5>Appointment</h5><p>555.014.2230<br>555.014.5932</p></div>
</section>

<!-- Footer -->
<footer class="abs footer">
  <div class="fcol" style="left:80px;width:320px">
    <h6>LATEST NEWS</h6>
    <div class="news"><i class="thumb"></i><p>New mailing options now ready for all clients.<small>6th June 2016</small></p></div>
    <div class="news"><i class="thumb"></i><p>New mailing options now ready for all clients.<small>6th June 2016</small></p></div>
  </div>
  <div class="fcol" style="left:450px">
    <h6>NEWSLETTER</h6>
    <p style="font-size:14px;line-height:1.5;width:300px">Sign up for our news and updates on mail services.</p>
    <div class="f-field">Email Id</div>
    <div class="f-btn">SUBSCRIBE</div>
  </div>
  <div class="fcol" style="left:810px">
    <h6>FOLLOW US</h6>
    <div class="social"><i></i>Chatterly</div>
    <div class="social"><i></i>Postwave</div>
    <div class="social"><i></i>Circlehub</div>
    <div class="social"><i></i>Linkfold</div>
  </div>
</footer>
<div class="abs copy">&copy; 2016 Lanta Voxmail Inc. All Rights Reserved.</div>

</body>
</html>
```